New business needs it's first website designed and coded for Wordpress

This is a new website for a new business. The business is called The Remote Tech Specialist (TRTS). The business is based across multiple countries with the goal of providing workers in the Philippines opportunities to find work in international companies based in Australia, Singapore and New Zealand. The target market for TRTS is large enterprises (initially in Australia) looking for well legally structured business that knows how to recruit the top IT professionals and ensure that they are happy, all compliance, taxes and legals and professionally done and all services contracts are local to ensure enforceability.

We are looking for 10 pages (6 templates) for the website as follows:
Home
About Us
Services
Work from home full-timers
Work from office full-times
Work from home contractors
Work from office contractors
Careers Job Search
Employers Contact Us
Candidates Register your interest

Target Market(s)

IT Professionals in the Philippines & large enterprises in Australia, Singapore and New Zealand

Industry/Entity Type

IT Recruitment

Coding

Coded - Design and coding required

Number of Pages Required

5+ page

Requirements
Must have
• Please based style off logo file attached.

```html
<!DOCTYPE html>
<html lang="en">
<head>
<meta charset="utf-8">
<title>The Remote Tech Specialist — IT Outsourcing Recruitment</title>
<link href="https://fonts.googleapis.com/css2?family=Poppins:wght@400;500;600;700&family=Michroma&display=swap" rel="stylesheet">
<style>
:root{
  --blue:#1aa7ec;
  --navy:#0b1d2f;
  --ink:#1b1f24;
  --muted:#6a6f75;
  --sky:#c9ecfb;
  --sky-soft:#dff3fc;
  --teal:#7b9fa8;
  --line:#e3e6e9;
  --white:#fff;
}
*{box-sizing:border-box;margin:0;padding:0}
html,body{width:1200px;height:4373px;overflow:hidden}
body{font-family:'Poppins',sans-serif;color:var(--ink);background:var(--white);position:relative}
.abs{position:absolute}
.wide{font-family:'Michroma',sans-serif}
.btn{position:absolute;background:var(--blue);color:#fff;font-size:12px;font-weight:500;display:flex;align-items:center;justify-content:center}

/* hero */
.hero{position:absolute;left:0;top:0;width:1200px;height:652px;background:linear-gradient(100deg,#1d2a3a 0%,#3b4654 45%,#6a6658 70%,#4a3a2c 100%)}
.topbar{position:absolute;top:0;left:0;width:1200px;height:48px;color:#fff;font-size:12px}
.topbar span{position:absolute;top:17px;display:flex;align-items:center;gap:10px}
.header{position:absolute;left:92px;top:49px;width:1016px;height:70px;background:#fff}
.brand{position:absolute;display:flex;align-items:center;gap:8px;font-weight:700;color:var(--navy)}
.brand .mark{width:14px;height:14px;background:var(--blue)}
.nav{position:absolute;top:27px;font-size:12px;font-weight:500;color:var(--ink)}
.get-started{position:absolute;right:0;top:0;width:171px;height:70px;background:var(--blue);clip-path:polygon(0 0,100% 0,100% 100%,22% 100%);color:#fff;font-size:13px;font-weight:500;display:flex;align-items:center;justify-content:flex-end;padding-right:29px}
.hero h1{position:absolute;left:139px;top:266px;font-size:54px;line-height:68px;font-weight:600;color:#fff;letter-spacing:.3px}
.hero p{position:absolute;left:141px;top:418px;width:560px;font-size:16px;line-height:23px;color:#fff}
.dots{position:absolute;left:562px;top:589px;display:flex;gap:6px}
.dots i{width:12px;height:3px;background:rgba(255,255,255,.5)}
.dots i.on{background:#fff}

/* about */
.photo{position:absolute}
.eyebrow{color:var(--blue);font-size:14px;font-weight:600;letter-spacing:3px}
.about-text{position:absolute;left:655px;top:766px;width:400px}
.about-text h2{font-size:24px;font-weight:500;margin:12px 0 8px;letter-spacing:.5px}
.about-text p{font-size:13px;line-height:25.5px;color:var(--muted)}

/* services */
.services{position:absolute;left:0;top:1242px;width:1200px;height:598px;background:var(--sky)}
.center{text-align:center;position:absolute;left:0;width:1200px}
.services h2{font-size:34px;font-weight:700;letter-spacing:3px}
.lead{font-size:13px;line-height:25px;color:var(--muted)}
.card{position:absolute;top:236px;width:287px;height:185px;background:#fff;padding:26px 24px}
.card h3{font-size:11px;font-weight:600;letter-spacing:.2px;margin-top:10px}
.card p{font-size:11px;line-height:18.5px;color:var(--muted);margin-top:30px}
.card svg{position:absolute;right:22px;top:18px}

/* why */
.why h2,.sec-title{font-family:'Michroma',sans-serif;font-size:25px;color:var(--ink)}
.step{position:absolute;top:1992px;width:220px;text-align:center}
.ring{width:140px;height:140px;border:1.5px dashed #8fcdf0;border-radius:50%;margin:0 auto;position:relative;display:flex;align-items:center;justify-content:center}
.ring .inner{width:118px;height:118px;border-radius:50%;background:#fff;box-shadow:0 4px 14px rgba(0,0,0,.12);display:flex;align-items:center;justify-content:center}
.ring .num{position:absolute;left:-6px;bottom:-2px;width:36px;height:36px;border-radius:50%;background:var(--blue);color:#fff;font-size:15px;display:flex;align-items:center;justify-content:center}
.step h3{font-size:17px;font-weight:500;margin-top:18px}
.step p{font-size:12.5px;line-height:19px;color:var(--muted);margin-top:6px}

/* testimonials */
.testi{position:absolute;left:0;top:2335px;width:1200px;height:467px;background:linear-gradient(90deg,#b9d6e3,#d8ebf3 40%,#cfe5ef 70%,#b5d3e1)}
.tcard{position:absolute;top:170px;width:295px;height:210px;background:#fff;border-radius:14px;padding:28px 24px}
.tcard p{font-size:12.5px;line-height:23px;color:var(--ink)}
.tcard .who{position:absolute;left:28px;bottom:22px;display:flex;align-items:center;gap:14px}
.avatar{width:46px;height:46px;border-radius:50%;background:linear-gradient(#cfd6dc,#9aa6b0)}
.who b{display:block;font-size:11.5px;font-weight:600}
.who small{font-size:10px}
.quote{position:absolute;right:22px;bottom:18px;font-family:'Poppins',sans-serif;font-size:70px;line-height:40px;color:#b8dff5;height:40px}
.arrow-btn{position:absolute;width:30px;height:30px;border-radius:50%;display:flex;align-items:center;justify-content:center}

/* jobs */
.job{position:absolute;left:141px;width:916px;height:127px;border:1.5px solid #8fcdf0;border-radius:8px;box-shadow:0 4px 12px rgba(26,167,236,.12)}
.job .logo{position:absolute;left:18px;top:35px;width:56px;height:56px;border-radius:50%;background:#f1f2f4;display:flex;align-items:center;justify-content:center}
.job .logo i{width:26px;height:26px;border-radius:50%}
.job .co{position:absolute;left:91px;top:44px;font-size:13px;font-weight:500}
.job .co small{display:block;font-size:11.5px;font-weight:400;color:var(--muted)}
.pill{position:absolute;width:176px;height:34px;background:#eef1f4;border-radius:4px;font-size:12.5px;display:flex;align-items:center;justify-content:center}
.under{position:absolute;width:176px;text-align:center;font-size:12.5px}
.apply{position:absolute;left:706px;top:44px;width:190px;height:34px;background:var(--blue);color:#fff;font-size:13px;font-weight:600;border-radius:3px;display:flex;align-items:center;justify-content:center;letter-spacing:.5px}
.pager{position:absolute;top:3554px;left:506px;display:flex;gap:4px}
.pager span{width:34px;height:34px;border:1.5px solid #9aa4ad;border-radius:4px;display:flex;align-items:center;justify-content:center;font-size:13px}
.pager .arr{border-color:var(--blue);color:var(--blue)}
.pager .on{background:var(--blue);border-color:var(--blue);color:#fff}

/* cta */
.cta{position:absolute;left:0;top:3674px;width:1200px;height:356px;background:linear-gradient(100deg,#7da1ab,#7a9ea8 60%,#86a9b2)}
.cta h2{font-family:'Michroma',sans-serif;font-size:35px;line-height:44px;color:var(--navy)}
.cta p{font-size:13.5px;line-height:22px;color:var(--navy)}

/* footer */
.footer{position:absolute;left:0;top:4030px;width:1200px;height:343px;background:var(--navy);color:#fff}
.footer h4{position:absolute;font-family:'Michroma',sans-serif;font-size:14.5px;font-weight:400}
.footer .txt{position:absolute;font-size:12px;line-height:22px}
.links{position:absolute;left:446px;top:118px;font-size:12px;line-height:24px;list-style:none}
.social{position:absolute;left:141px;top:232px;display:flex;gap:12px}
.social i{width:26px;height:26px;border:1.5px solid #fff;border-radius:50%}
.contact-item{position:absolute;left:865px;display:flex;gap:12px;font-size:12px;line-height:16px}
.contact-item b{font-weight:500;display:block}
.copy{position:absolute;left:0;top:310px;width:1200px;text-align:center;font-size:12px}
.rule{position:absolute;left:141px;top:294px;width:916px;height:1px;background:rgba(255,255,255,.18)}
</style>
</head>
<body>

<!-- HERO -->
<section class="hero">
  <div class="abs" role="img" aria-label="Young IT professional relaxing at a desk with laptop and coffee in a modern office" style="inset:0;background:linear-gradient(90deg,rgba(11,29,47,.75),rgba(11,29,47,.25))"></div>
  <div class="topbar">
    <span style="left:92px">TheRemoteTech Outsourcing Recruitment</span>
    <span style="left:798px"><svg width="14" height="14" viewBox="0 0 24 24" fill="#fff"><path d="M6.6 10.8a15 15 0 0 0 6.6 6.6l2.2-2.2c.3-.3.7-.4 1-.2 1.1.4 2.3.6 3.6.6.6 0 1 .4 1 1V20c0 .6-.4 1-1 1A17 17 0 0 1 3 4c0-.6.4-1 1-1h3.5c.6 0 1 .4 1 1 0 1.3.2 2.5.6 3.6.1.3 0 .7-.2 1z"/></svg>123.456.7890</span>
    <span style="left:950px"><svg width="16" height="12" viewBox="0 0 24 18" fill="#fff"><path d="M0 0h24v18H0z" fill="#fff"/><path d="M1 1l11 8 11-8" stroke="#3b4654" stroke-width="2" fill="none"/></svg>info@trtsglobal.com</span>
  </div>
  <header class="header">
    <div class="brand" style="left:22px;top:22px"><span class="mark"></span><span style="font-size:22px;letter-spacing:1px">TRTS</span><span style="font-size:8px;line-height:9px;font-weight:600">THE REMOTE<br>TECH SPECIALIST</span></div>
    <span class="nav" style="left:259px">Home</span>
    <span class="nav" style="left:320px">About Us</span>
    <span class="nav" style="left:402px">Services</span>
    <span class="nav" style="left:482px">Why Choose Us</span>
    <span class="nav" style="left:602px">Testimonials</span>
    <span class="nav" style="left:705px">Career</span>
    <span class="nav" style="left:772px">Contact Us</span>
    <div class="get-started">Get Started</div>
  </header>
  <h1>Connecting Top IT Talent<br>with Global Opportunities</h1>
  <p>Providing skilled professionals from the Philippines to enterprises in Australia, Singapore, and New Zealand.</p>
  <div class="btn" style="left:141px;top:483px;width:132px;height:38px">LET'S CONNECT</div>
  <div class="dots"><i></i><i class="on"></i><i></i><i></i><i></i></div>
</section>

<!-- ABOUT -->
<section>
  <div class="photo" role="img" aria-label="Hands typing on a laptop in a blue-lit office" style="left:141px;top:774px;width:215px;height:383px;background:linear-gradient(160deg,#14324d,#3d6c8d 55%,#c9d3da)"></div>
  <div class="photo" role="img" aria-label="Smiling businessman in glasses and suit" style="left:382px;top:742px;width:215px;height:381px;background:linear-gradient(170deg,#1f3344,#3a5466 50%,#1c2633)"></div>
  <div class="abs" style="left:295px;top:916px;width:150px;height:111px;background:#fff;display:flex;align-items:center;justify-content:center;gap:6px">
    <span style="width:10px;height:10px;background:var(--blue)"></span><span style="font-size:26px;font-weight:700;color:var(--navy);letter-spacing:1px">TRTS</span>
  </div>
  <div class="about-text">
    <div class="eyebrow">WHY CHOOSE US</div>
    <h2>THEREMOTETECH OUTSOURCING</h2>
    <p>Lorem Ipsum is simply dummy text of the printing and typesetting industry. Lorem Ipsum has been the industry's standard dummy text ever since the 1500s, when an unknown printer took a galley of type and scrambled it to make a type specimen book. It has survived not only five centuries, but also the leap into electronic typesetting, remaining essentially unchanged.</p>
  </div>
  <div class="btn" style="left:655px;top:1035px;width:119px;height:38px">Learn More</div>
</section>

<!-- SERVICES -->
<section class="services">
  <div class="center eyebrow" style="top:82px;font-size:13px">OUR SERVICES</div>
  <h2 class="center" style="top:103px">WHAT WE DO</h2>
  <p class="center lead" style="top:160px">Lorem Ipsum is simply dummy text of the printing and typesetting industry. Lorem Ipsum has been the industry's<br>standard dummy text ever since</p>
  <div class="card" style="left:141px">
    <svg width="36" height="36" viewBox="0 0 36 36" fill="none" stroke="#222" stroke-width="1.5"><circle cx="18" cy="18" r="9"/><circle cx="18" cy="15" r="3"/><path d="M12 24c2-4 10-4 12 0"/><path d="M18 3v4M18 29v4M3 18h4M29 18h4M7 7l3 3M26 26l3 3M29 7l-3 3M10 26l-3 3"/></svg>
    <h3>RECRUITMENT &amp; OUTSOURCING</h3>
    <p>Lorem Ipsum is simply dummy text of the printing and typesetting industry. Lorem Ipsum has been the industry's standard dummy text ever since.</p>
  </div>
  <div class="card" style="left:455px">
    <svg width="36" height="36" viewBox="0 0 36 36" fill="none" stroke="#222" stroke-width="1.5"><path d="M7 3h16l6 6v24H7z"/><path d="M11 11h10M11 16h14M11 21h6"/><path d="M20 30v-6M24 30v-9M28 30v-4"/></svg>
    <h3>COMPLIANCE &amp; LEGAL ASSURANCE</h3>
    <p>Lorem Ipsum is simply dummy text of the printing and typesetting industry. Lorem Ipsum has been the industry's standard dummy text ever since.</p>
  </div>
  <div class="card" style="left:770px">
    <svg width="36" height="36" viewBox="0 0 36 36" fill="none" stroke="#222" stroke-width="1.5"><circle cx="18" cy="18" r="13"/><circle cx="18" cy="14" r="4"/><path d="M11 26c2-5 12-5 14 0"/><path d="M4 10l3 2M32 10l-3 2M18 2v3"/></svg>
    <h3>TALENT RETENTION &amp; SATISFACTION</h3>
    <p>Lorem Ipsum is simply dummy text of the printing and typesetting industry. Lorem Ipsum has been the industry's standard dummy text ever since.</p>
  </div>
  <div class="arrow-btn" style="left:481px;top:408px;width:27px;height:27px;background:var(--blue)"><svg width="10" height="10" viewBox="0 0 10 10" stroke="#fff" stroke-width="1.5" fill="none"><path d="M2 8l6-6M3 2h5v5"/></svg></div>
  <div class="btn" style="left:521px;top:472px;width:120px;height:37px">Learn More</div>
</section>

<!-- WHY CHOOSE -->
<section class="why">
  <h2 class="center" style="top:1926px">Why Choose Us?</h2>
  <div class="step" style="left:184px">
    <div class="ring"><div class="inner"><svg width="52" height="52" viewBox="0 0 52 52" fill="none" stroke="#222" stroke-width="1.6"><path d="M12 6h22l6 6v30H12z"/><path d="M17 16h14M17 22h14M17 28h8"/><circle cx="34" cy="36" r="7"/><path d="M31 36l2 2 4-4"/></svg></div><span class="num">1</span></div>
    <h3>Legal Compliance</h3>
    <p>Lorem ipsum dolor sit consectetuer adipiscing elit, sed diam nonumy nibh euismod tincidunt ut.</p>
  </div>
  <div class="step" style="left:489px">
    <div class="ring"><div class="inner"><svg width="52" height="52" viewBox="0 0 52 52" fill="none" stroke="#222" stroke-width="1.6"><circle cx="26" cy="26" r="19"/><circle cx="26" cy="22" r="5"/><path d="M16 36c3-7 17-7 20 0"/><path d="M26 5l1.5 3 3 .5-2 2 .5 3-3-1.5-3 1.5.5-3-2-2 3-.5z"/></svg></div><span class="num">2</span></div>
    <h3>Local Service Contracts</h3>
    <p>Lorem ipsum dolor sit consectetuer adipiscing elit, sed diam nonumy nibh euismod tincidunt ut.</p>
  </div>
  <div class="step" style="left:795px">
    <div class="ring"><div class="inner"><svg width="52" height="52" viewBox="0 0 52 52" fill="none" stroke="#222" stroke-width="1.6"><circle cx="26" cy="20" r="8"/><path d="M16 20a10 10 0 0 1 20 0"/><rect x="14" y="18" width="4" height="7"/><rect x="34" y="18" width="4" height="7"/><path d="M12 44c2-9 26-9 28 0"/></svg></div><span class="num">3</span></div>
    <h3>Expert Recruitment</h3>
    <p>Lorem ipsum dolor sit consectetuer adipiscing elit, sed diam nonumy nibh euismod tincidunt ut.</p>
  </div>
  <svg class="abs" style="left:415px;top:2050px" width="70" height="24" viewBox="0 0 70 24" fill="none" stroke="#777" stroke-width="1.6"><path d="M2 10q30-14 62 8"/><path d="M56 18l8 0-3-7"/></svg>
  <svg class="abs" style="left:720px;top:2050px" width="70" height="24" viewBox="0 0 70 24" fill="none" stroke="#777" stroke-width="1.6"><path d="M2 16q30 10 62-8"/><path d="M56 5l8 3-4 7"/></svg>
</section>

<!-- TESTIMONIALS -->
<section class="testi" role="img" aria-label="Soft blue photo of a person at work behind the testimonials">
  <div class="center" style="top:84px;color:var(--blue);font-size:14.5px">CLIENT SUCCESS STORIES</div>
  <h2 class="center sec-title" style="top:106px">What Our Customers Are Saying</h2>
  <div class="tcard" style="left:141px">
    <p>Lorem ipsum dolor sit amet, is notthere's consectetuer adipiscing elit, sed diam nonummy nibh euismod tincidunt utted laoreet dolore magna aliquam.</p>
    <div class="who"><span class="avatar"></span><div><b>John Doe</b><small>Freelancer</small></div></div>
    <span class="quote">”</span>
  </div>
  <div class="tcard" style="left:453px">
    <p>Lorem ipsum dolor sit amet, is notthere's consectetuer adipiscing elit, sed diam nonummy nibh euismod tincidunt utted laoreet dolore magna aliquam.</p>
    <div class="who"><span class="avatar"></span><div><b>Lisa thomas</b><small>Sr. Developer</small></div></div>
    <span class="quote">”</span>
  </div>
  <div class="tcard" style="left:764px">
    <p>Lorem ipsum dolor sit amet, is notthere's consectetuer adipiscing elit, sed diam nonummy nibh euismod tincidunt utted laoreet dolore magna aliquam.</p>
    <div class="who"><span class="avatar"></span><div><b>Jonathan Stem</b><small>Project Manager</small></div></div>
    <span class="quote">”</span>
  </div>
  <div class="arrow-btn" style="left:89px;top:260px;background:#fff;border:1px solid #ccc"><svg width="12" height="12" viewBox="0 0 12 12" stroke="#222" stroke-width="1.8" fill="none"><path d="M11 6H1M5 2L1 6l4 4"/></svg></div>
  <div class="arrow-btn" style="left:1080px;top:260px;background:var(--blue);box-shadow:0 0 0 3px #fff"><svg width="12" height="12" viewBox="0 0 12 12" stroke="#fff" stroke-width="1.8" fill="none"><path d="M1 6h10M7 2l4 4-4 4"/></svg></div>
</section>

<!-- JOBS -->
<section>
  <h2 class="center sec-title" style="top:2883px">Latest Job Openings</h2>

  <div class="job" style="top:2946px">
    <div class="logo"><i style="background:linear-gradient(#f2a65a,#d9468f)"></i></div>
    <div class="co">Company Name<small>www.xyz.com</small></div>
    <div class="pill" style="left:253px;top:22px;font-weight:500">Sr. Web Developer</div>
    <div class="under" style="left:253px;top:63px;font-weight:600">Full-Time</div>
    <div class="pill" style="left:478px;top:22px">Salary: $18 - $20 p/h</div>
    <div class="under" style="left:478px;top:63px;color:var(--muted)">Australia</div>
    <div class="apply">APPLY NOW</div>
  </div>
  <div class="job" style="top:3094px">
    <div class="logo"><i style="background:linear-gradient(#6b5bd6,#f2b33a);border-radius:6px"></i></div>
    <div class="co">Company Name<small>www.xyz.com</small></div>
    <div class="pill" style="left:253px;top:22px;font-weight:500">Sr. Web Developer</div>
    <div class="under" style="left:253px;top:63px;font-weight:600">Full-Time</div>
    <div class="pill" style="left:478px;top:22px">Salary: $18 - $20 p/h</div>
    <div class="under" style="left:478px;top:63px;color:var(--muted)">Singapore</div>
    <div class="apply">APPLY NOW</div>
  </div>
  <div class="job" style="top:3243px">
    <div class="logo"><i style="background:linear-gradient(#e94a3a,#c7281c)"></i></div>
    <div class="co">Company Name<small>www.xyz.com</small></div>
    <div class="pill" style="left:253px;top:22px;font-weight:500">Sr. Web Developer</div>
    <div class="under" style="left:253px;top:63px;font-weight:600">Full-Time</div>
    <div class="pill" style="left:478px;top:22px">Salary: $18 - $20 p/h</div>
    <div class="under" style="left:478px;top:63px;color:var(--muted)">New Zealand</div>
    <div class="apply">APPLY NOW</div>
  </div>
  <div class="job" style="top:3391px">
    <div class="logo"><i style="background:linear-gradient(#f2a65a,#d9468f)"></i></div>
    <div class="co">Company Name<small>www.xyz.com</small></div>
    <div class="pill" style="left:253px;top:22px;font-weight:500">Sr. Web Developer</div>
    <div class="under" style="left:253px;top:63px;font-weight:600">Full-Time</div>
    <div class="pill" style="left:478px;top:22px">Salary: $18 - $20 p/h</div>
    <div class="under" style="left:478px;top:63px;color:var(--muted)">Australia</div>
    <div class="apply">APPLY NOW</div>
  </div>

  <div class="pager">
    <span class="arr"><svg width="18" height="12" viewBox="0 0 18 12" stroke="currentColor" stroke-width="1.8" fill="none"><path d="M17 6H1M6 1L1 6l5 5"/></svg></span>
    <span style="margin-left:4px">1</span><span class="on">2</span><span>3</span>
    <span class="arr" style="margin-left:4px"><svg width="18" height="12" viewBox="0 0 18 12" stroke="currentColor" stroke-width="1.8" fill="none"><path d="M1 6h16M12 1l5 5-5 5"/></svg></span>
  </div>
</section>

<!-- CTA -->
<section class="cta">
  <h2 class="center" style="top:80px">Invite Both Candidates And<br>Employers To Engage Further</h2>
  <p class="center" style="top:170px">Lorem Ipsum is simply dummy text &nbsp;printing and typesetting industry. Lorem Ipsum has been<br>the industry's standard du ever since the 1500s, when an unknown printer took</p>
  <div class="abs" style="left:512px;top:3917px;margin-top:-3674px;width:175px;height:41px;background:var(--navy);color:#fff;font-size:12px;display:flex;align-items:center;padding-left:14px;gap:20px">Contact Us Today
    <span style="width:35px;height:35px;background:#fff;display:flex;align-items:center;justify-content:center"><svg width="22" height="18" viewBox="0 0 22 18" stroke="var(--navy)" stroke-width="2.2" fill="none"><path d="M1 9h20M13 1l8 8-8 8"/></svg></span>
  </div>
</section>

<!-- FOOTER -->
<footer class="footer">
  <div class="brand" style="left:141px;top:72px;color:#fff"><span class="mark"></span><span style="font-size:26px;letter-spacing:1px">TRTS</span><span style="font-size:9px;line-height:10px;font-weight:600">THE REMOTE<br>TECH SPECIALIST</span></div>
  <p class="txt" style="left:141px;top:116px;width:260px">Lorem Ipsum is simply dummy &nbsp;printing and typesetting industry. Lorem Ipsum has been the industry's standard</p>
  <h4 style="left:141px;top:205px">Follow Us</h4>
  <div class="social"><i></i><i></i><i></i><i></i></div>

  <h4 style="left:441px;top:78px">Quick Links</h4>
  <ul class="links"><li>Home</li><li>About Us</li><li>Services</li><li>Jobs</li><li>Career</li><li>Contact Us</li></ul>

  <h4 style="left:602px;top:78px">Newsletter Sign Up</h4>
  <p class="txt" style="left:603px;top:116px;width:230px;line-height:20px">Subscribe to our newsletter to get the latest update to your inbox</p>
  <div class="abs" style="left:603px;top:168px;width:216px;height:33px;background:#fff;color:#888;font-size:10px;padding:10px 11px">Your Email*</div>
  <div class="abs" style="left:603px;top:216px;width:216px;height:32px;background:var(--blue);font-size:12px;display:flex;align-items:center;justify-content:center">SUBSCRIBE</div>

  <h4 style="left:865px;top:78px">Contact Details</h4>
  <div class="contact-item" style="top:118px"><svg width="12" height="16" viewBox="0 0 12 16" fill="#fff"><path d="M6 0a6 6 0 0 0-6 6c0 4.5 6 10 6 10s6-5.5 6-10a6 6 0 0 0-6-6zm0 8.5A2.5 2.5 0 1 1 6 3.5a2.5 2.5 0 0 1 0 5z"/></svg><div><b>Address</b>123, Building Name, Street<br>City, State XY 123456</div></div>
  <div class="contact-item" style="top:185px"><svg width="13" height="13" viewBox="0 0 24 24" fill="#fff"><path d="M6.6 10.8a15 15 0 0 0 6.6 6.6l2.2-2.2c.3-.3.7-.4 1-.2 1.1.4 2.3.6 3.6.6.6 0 1 .4 1 1V20c0 .6-.4 1-1 1A17 17 0 0 1 3 4c0-.6.4-1 1-1h3.5c.6 0 1 .4 1 1 0 1.3.2 2.5.6 3.6.1.3 0 .7-.2 1z"/></svg><div><b>Phone</b>(123) 456-7890</div></div>
  <div class="contact-item" style="top:236px"><svg width="14" height="11" viewBox="0 0 24 18"><path d="M0 0h24v18H0z" fill="#fff"/><path d="M1 1l11 8 11-8" stroke="#0b1d2f" stroke-width="2" fill="none"/></svg><div><b>Email</b>info@trtsglobal.com</div></div>

  <div class="rule"></div>
  <div class="copy">Copyright © 2025 The Remote Tech Specialist. All Rights Reserved.</div>
</footer>

</body>
</html>
```